Powerpoint design for Summit Lane Advisors

We would like to have a Power point template/design with flexibilities and good opportunities to do changes.
• Be able to change in image background
• Themes are SLA colors and complementary colors. Please come with suggestions.
• Alternate white and blue background
• Standard functions and opportunities within Powerpoint should be able to be used or be accessible.
• Feel free to change/alter the logo for example remove or separate the text in the logo ("Summit Lane Advisors" ) and the tagline ("we create competitiveness")
• www.summitlaneadvisors.se

```html
<!DOCTYPE html>
<html lang="en">
<head>
<meta charset="utf-8">
<title>Summit Lane Advisors – Presentation Template</title>
<link rel="stylesheet" href="https://fonts.googleapis.com/css2?family=Montserrat:wght@400;500;600;700&display=swap">
<style>
:root{
  --navy:#0b4a92;
  --navy-dark:#06346d;
  --orange:#f28a1c;
  --ink:#222426;
  --grey:#6b6d70;
  --light:#eef0f3;
  --canvas:#b0afb2;
  --white:#ffffff;
}
*{box-sizing:border-box;margin:0;padding:0}
html,body{width:1200px;height:3632px;overflow:hidden}
body{background:var(--canvas);font-family:"Montserrat",sans-serif;color:var(--ink);position:relative}
.slide{position:absolute;width:540px;height:303px;overflow:hidden;background:var(--white)}
.abs{position:absolute}
.photo{position:absolute}
.ph-dark{background:radial-gradient(ellipse at 75% 20%,#b0602a 0%,#5a3524 30%,#1a1614 65%,#0b0b0c 100%)}
.ph-blue{background:linear-gradient(120deg,#0b3f7e 0%,#1d5fa8 45%,#5a8fc6 75%,#27528a 100%)}
.ph-light{background:linear-gradient(120deg,#f4f6f9 0%,#dfe6ee 45%,#c5d3e3 75%,#eef1f5 100%)}
.ph-tablet{background:linear-gradient(135deg,#d8c9b6 0%,#eae2d6 40%,#b8c7d8 70%,#8fa6c0 100%)}
.ph-cart{background:linear-gradient(135deg,#7c4a34 0%,#c9865a 35%,#e7c8a7 60%,#9bb0c8 100%)}
.ph-map{background:linear-gradient(100deg,#0d0e10 0%,#1b1d22 40%,#3f4650 70%,#6e7985 100%)}
.ph-team{background:linear-gradient(180deg,#0d3c78 0%,#2a64a6 60%,#0b4a92 100%)}
.ph-face{background:radial-gradient(circle at 50% 40%,#c9c3bd 0%,#8f8a86 100%)}

.h-orange{color:var(--orange);font-weight:700}
.h-white{color:var(--white)}
.h-navy{color:var(--navy);font-weight:600}
.body-s{font-size:6.2px;line-height:1.3;color:var(--ink)}
.body-xs{font-size:5.2px;line-height:1.3;color:var(--grey)}
.date{font-size:6.5px}
.copy{font-size:4.5px;color:#9aa0a8}

.cover-title{font-size:25px;line-height:1.02;font-weight:700;letter-spacing:-0.3px}
.cover-sub{font-size:14px;line-height:1.05;font-weight:500}

.brand{position:absolute;text-align:center;font-weight:600}
.brand .mark{display:block;font-size:25px;line-height:1;letter-spacing:1px}
.brand .name{display:block;font-size:9px;margin-top:2px}

.foot-orange{position:absolute;left:0;top:281px;width:24px;height:6px;background:var(--orange)}
.foot-logo{position:absolute;left:28px;top:272px;font-size:15px;font-weight:700;color:var(--navy);letter-spacing:.5px}
.foot-band{position:absolute;left:66px;right:0;top:281px;height:6px;background:var(--navy)}
.foot-band span{position:absolute;right:38px;top:0.5px;font-size:4.2px;color:var(--white)}
.foot-page{position:absolute;right:14px;top:279px;width:10px;height:10px;background:var(--orange);font-size:5px;color:var(--white);text-align:center;line-height:10px}

.slide-title{position:absolute;left:0;right:0;top:24px;text-align:center;font-size:18px;color:var(--ink)}
.slide-title b{color:var(--navy);font-weight:700}
.item-title{font-size:8.5px;font-weight:500}
.t-navy{color:var(--navy)}
.t-orange{color:var(--orange)}
.bullets{list-style:none;font-size:8px;line-height:1.55}
.bullets li::before{content:"";display:inline-block;width:4px;height:4px;background:var(--orange);border-radius:50%;margin-right:8px;vertical-align:middle}
.icon-c{position:absolute;border-radius:50%;display:flex;align-items:center;justify-content:center}
.icon-c svg{width:55%;height:55%}
.bg-navy{background:var(--navy)}
.bg-orange{background:var(--orange)}
.bg-ink{background:var(--ink)}
.bg-grey{background:#c8cacd}

table.data{position:absolute;left:38px;top:79px;width:464px;border-collapse:collapse;font-size:7px}
table.data th{background:var(--navy);color:var(--white);font-weight:500;height:29px;text-align:center;border:1px solid #fff}
table.data th:first-child{text-align:left;padding-left:5px}
table.data th.hl{background:var(--orange)}
table.data td{height:31px;text-align:center;border:1px solid #cfd3d8}
table.data td:first-child{text-align:left;padding-left:5px}
.contact{font-size:7px;color:var(--white);line-height:1.9}
.contact svg{width:7px;height:7px;vertical-align:-1px;margin-right:6px}
</style>
</head>
<body>

<svg width="0" height="0" style="position:absolute" aria-hidden="true">
  <defs>
    <symbol id="i-bulb" viewBox="0 0 24 24"><circle cx="12" cy="9" r="6" fill="#fff"/><rect x="9" y="15" width="6" height="5" rx="1" fill="#fff"/></symbol>
    <symbol id="i-search" viewBox="0 0 24 24"><circle cx="10" cy="10" r="6" fill="none" stroke="#fff" stroke-width="2.5"/><line x1="14.5" y1="14.5" x2="21" y2="21" stroke="#fff" stroke-width="3" stroke-linecap="round"/></symbol>
    <symbol id="i-monitor" viewBox="0 0 24 24"><rect x="3" y="4" width="18" height="12" rx="1" fill="none" stroke="#fff" stroke-width="2.2"/><rect x="10" y="16" width="4" height="3" fill="#fff"/><rect x="7" y="19" width="10" height="2" fill="#fff"/></symbol>
    <symbol id="i-doc" viewBox="0 0 24 24"><rect x="5" y="3" width="14" height="18" rx="1.5" fill="none" stroke="#fff" stroke-width="2"/><line x1="8" y1="8" x2="16" y2="8" stroke="#fff" stroke-width="1.6"/><line x1="8" y1="12" x2="16" y2="12" stroke="#fff" stroke-width="1.6"/><line x1="8" y1="16" x2="16" y2="16" stroke="#fff" stroke-width="1.6"/></symbol>
    <symbol id="i-tools" viewBox="0 0 24 24"><line x1="4" y1="20" x2="18" y2="6" stroke="#fff" stroke-width="2.6" stroke-linecap="round"/><line x1="4" y1="6" x2="18" y2="20" stroke="#fff" stroke-width="2.6" stroke-linecap="round"/><circle cx="18" cy="6" r="3" fill="#fff"/></symbol>
    <symbol id="i-chart" viewBox="0 0 24 24"><rect x="4" y="13" width="4" height="7" fill="#fff"/><rect x="10" y="9" width="4" height="11" fill="#fff"/><rect x="16" y="5" width="4" height="15" fill="#fff"/></symbol>
    <symbol id="i-shield" viewBox="0 0 24 24"><path d="M12 3 L20 6 V12 C20 17 16 20 12 21 C8 20 4 17 4 12 V6 Z" fill="#fff"/></symbol>
    <symbol id="i-gears" viewBox="0 0 24 24"><circle cx="9" cy="13" r="5" fill="none" stroke="#fff" stroke-width="2.4"/><circle cx="17" cy="8" r="3.5" fill="none" stroke="#fff" stroke-width="2"/></symbol>
    <symbol id="i-phone" viewBox="0 0 24 24"><path d="M6 3 L10 3 L11 8 L8.5 9.5 C9.5 12 12 14.5 14.5 15.5 L16 13 L21 14 L21 18 C21 19.5 19.5 21 18 21 C10 20 4 14 3 6 C3 4.5 4.5 3 6 3 Z" fill="#fff"/></symbol>
    <symbol id="i-at" viewBox="0 0 24 24"><circle cx="12" cy="12" r="4" fill="none" stroke="#fff" stroke-width="2.4"/><path d="M16 12 V14 C16 17 21 17 21 12 A9 9 0 1 0 16 20" fill="none" stroke="#fff" stroke-width="2.4"/></symbol>
    <symbol id="i-globe" viewBox="0 0 24 24"><circle cx="12" cy="12" r="9" fill="none" stroke="#fff" stroke-width="2"/><ellipse cx="12" cy="12" rx="4" ry="9" fill="none" stroke="#fff" stroke-width="1.6"/><line x1="3" y1="12" x2="21" y2="12" stroke="#fff" stroke-width="1.6"/></symbol>
  </defs>
</svg>

<!-- Hero cover -->
<section class="slide" style="left:330px;top:92px">
  <div class="photo ph-dark" style="left:0;top:0;width:540px;height:230px" role="img" aria-label="Dark photo of a hand holding a tablet with business charts, warm orange light"></div>
  <div class="abs" style="left:48px;top:52px">
    <div class="cover-title h-orange">Presentation Title<br>Goes Here!</div>
    <div class="cover-sub h-white" style="margin-top:10px">Subtitle of Presentation<br>Goes Here!</div>
    <div class="date h-white" style="margin-top:18px">Sunday, April 18, 2021</div>
  </div>
  <div class="copy abs" style="left:48px;top:263px">© Copyright Summit Lane Advisors</div>
  <div class="brand t-navy" style="right:24px;top:236px"><span class="mark">SLA</span><span class="name">Summit Lane Advisors</span></div>
</section>

<!-- Row 1 -->
<section class="slide" style="left:51px;top:673px">
  <div class="photo ph-blue" style="left:0;top:0;width:540px;height:229px" role="img" aria-label="Blue-toned photo of a shopping cart with business charts"></div>
  <div class="abs h-white" style="left:50px;top:44px">
    <div style="font-size:15px;font-weight:500">We Create</div>
    <div style="font-size:25px;font-weight:700;line-height:1.1;letter-spacing:-0.3px">Digital Competitiveness</div>
    <div class="cover-sub" style="margin-top:6px">Subtitle of Presentation<br>Goes Here!</div>
    <div class="date" style="margin-top:20px">Sunday, April 18, 2021</div>
  </div>
  <div class="copy abs" style="left:50px;top:262px">© Copyright Summit Lane Advisors</div>
  <div class="brand t-navy" style="right:24px;top:234px"><span class="mark">SLA</span><span class="name">Summit Lane Advisors</span></div>
</section>

<section class="slide" style="left:609px;top:673px">
  <div class="photo ph-light" style="left:0;top:0;width:540px;height:223px" role="img" aria-label="Light photo of a person working on a tablet with charts"></div>
  <div class="abs" style="left:50px;top:44px">
    <div class="cover-title t-navy">Presentation Title<br>Goes Here!</div>
    <div class="cover-sub" style="margin-top:8px">Subtitle of Presentation<br>Goes Here!</div>
    <div class="date" style="margin-top:18px">Sunday, April 18, 2021</div>
  </div>
  <div class="abs bg-navy" style="left:0;top:223px;width:540px;height:80px"></div>
  <div class="copy abs" style="left:50px;top:262px;color:#c9d6e8">© Copyright Summit Lane Advisors</div>
  <div class="brand h-white" style="right:24px;top:234px"><span class="mark">SLA</span><span class="name">Summit Lane Advisors</span></div>
</section>

<!-- Row 2 -->
<section class="slide" style="left:51px;top:994px">
  <div class="photo ph-dark" style="left:0;top:0;width:540px;height:229px" role="img" aria-label="Dark photo of a hand holding a tablet with business charts, warm orange light"></div>
  <div class="abs" style="left:50px;top:44px">
    <div class="cover-title h-orange">Presentation Title<br>Goes Here!</div>
    <div class="cover-sub h-white" style="margin-top:8px">Subtitle of Presentation<br>Goes Here!</div>
    <div class="date h-white" style="margin-top:18px">Sunday, April 18, 2021</div>
  </div>
  <div class="copy abs" style="left:50px;top:262px">© Copyright Summit Lane Advisors</div>
  <div class="brand t-navy" style="right:24px;top:234px"><span class="mark">SLA</span><span class="name">Summit Lane Advisors</span></div>
</section>

<section class="slide" style="left:609px;top:994px">
  <div class="abs" style="left:0;right:0;top:26px;text-align:center;font-size:18px;font-weight:700">About Summit Lane Advisors</div>
  <div class="photo ph-tablet" style="left:0;top:72px;width:540px;height:96px" role="img" aria-label="Photo of a tablet showing a business report with pie charts"></div>
  <div class="abs bg-navy h-white" style="left:0;top:166px;width:540px;height:17px;font-size:8.5px;text-align:center;line-height:17px">Our passion is the key factor for customer success</div>
  <div class="abs body-s" style="left:40px;right:40px;top:201px;text-align:center;color:#444">Digital transformation is changing the way we live, what we do and how we communicate with each other as well as how we do our business and shopping.<br>The customers are better informed and more independent in their decisions. The digital transformation has created great possibilities in more channels than ever.</div>
  <div class="foot-orange"></div><div class="foot-logo">SLA</div>
  <div class="foot-band"><span>© Copyright Summit Lane Advisors</span></div><div class="foot-page">4</div>
</section>

<!-- Row 3 -->
<section class="slide" style="left:51px;top:1316px">
  <div class="abs bg-navy" style="left:0;top:0;width:540px;height:140px"></div>
  <div class="abs h-white" style="left:0;right:0;top:26px;text-align:center;font-size:19px;font-weight:600">Digital Development and Transformation</div>
  <div class="abs h-white" style="left:56px;right:56px;top:60px;text-align:center;font-size:6px;line-height:1.25">To get knowledge about how products, services and information can be consumed with digital concepts and solutions is more necessary than ever for companies. They need this to adapt to their customers wishes and requirements. It is essential to go from believing to knowing to implementing. Using the knowledge about digital development and concepts gives companies the right background to invest in digital solutions. This creates competitiveness and new business opportunities in a global environment.</div>
  <div class="icon-c bg-navy" style="left:62px;top:115px;width:52px;height:52px;border:3px solid #fff"><svg><use href="#i-bulb"/></svg></div>
  <div class="icon-c bg-orange" style="left:182px;top:115px;width:52px;height:52px;border:3px solid #fff"><svg><use href="#i-tools"/></svg></div>
  <div class="icon-c bg-navy" style="left:302px;top:115px;width:52px;height:52px;border:3px solid #fff"><svg><use href="#i-monitor"/></svg></div>
  <div class="icon-c bg-orange" style="left:422px;top:115px;width:52px;height:52px;border:3px solid #fff"><svg><use href="#i-chart"/></svg></div>
  <div class="abs" style="left:38px;top:172px;width:100px;text-align:center"><div class="t-navy" style="font-size:7.5px">Our Passion</div><div class="body-xs" style="margin-top:8px">Our team's passion is to understand and follow the digital transformation and development and to use this knowledge to help customers to gain competitiveness.</div></div>
  <div class="abs" style="left:158px;top:172px;width:100px;text-align:center"><div class="t-orange" style="font-size:7.5px;line-height:1">Concept<br>Development</div><div class="body-xs" style="margin-top:4px">Together with our customers we identify the business opportunities and challenges and develop concepts according to this. The concepts include proposed digital solutions and best praxis.</div></div>
  <div class="abs" style="left:278px;top:172px;width:100px;text-align:center"><div class="t-navy" style="font-size:7.5px;line-height:1">Concept<br>Implementation</div><div class="body-xs" style="margin-top:4px">New concepts and solutions are very dependent on a good implementation plan to be successful. Together with the customer we work out the best set-up.</div></div>
  <div class="abs" style="left:398px;top:172px;width:100px;text-align:center"><div class="t-orange" style="font-size:7.5px;line-height:1">Analytics And<br>Evaluation</div><div class="body-xs" style="margin-top:4px">Before, during and after concept development it is crucial to regularly do analytics and evaluation. The result of this will be used to improve and refine concept development and concept implementation.</div></div>
  <div class="foot-orange"></div><div class="foot-logo">SLA</div>
  <div class="foot-band"><span>© Copyright Summit Lane Advisors</span></div><div class="foot-page">5</div>
</section>

<section class="slide" style="left:609px;top:1316px">
  <div class="photo ph-team" style="left:0;top:0;width:540px;height:125px" role="img" aria-label="Blue-toned photo of a business team standing by office windows"></div>
  <div class="abs h-white" style="left:0;right:0;top:26px;text-align:center;font-size:19px">Our <b style="font-weight:600">Team</b></div>
  <div class="photo ph-face" style="left:72px;top:70px;width:72px;height:72px;border-radius:50%;border:3px solid #fff" role="img" aria-label="Portrait photo of team member"></div>
  <div class="photo ph-face" style="left:234px;top:70px;width:72px;height:72px;border-radius:50%;border:3px solid #fff" role="img" aria-label="Portrait photo of team member"></div>
  <div class="photo ph-face" style="left:396px;top:70px;width:72px;height:72px;border-radius:50%;border:3px solid #fff" role="img" aria-label="Portrait photo of team member"></div>
  <div class="abs" style="left:38px;top:150px;width:140px;text-align:center"><div class="t-navy" style="font-size:10px;font-weight:600">Person Name</div><div class="t-orange" style="font-size:6px">Job Title Goes Here!</div><div class="body-xs" style="margin-top:12px;color:#333">Lorem ipsum dolor sit amet, at laborum nibh duis mauris. Per ultrices lectus sed metus tristique eu. Diam suspendisse ac ipsum maecenas fermentum, aliquet imperdiet et lobortis.</div></div>
  <div class="abs" style="left:200px;top:150px;width:140px;text-align:center"><div class="t-navy" style="font-size:10px;font-weight:600">Person Name</div><div class="t-orange" style="font-size:6px">Job Title Goes Here!</div><div class="body-xs" style="margin-top:12px;color:#333">Lorem ipsum dolor sit amet, at laborum nibh duis mauris. Per ultrices lectus sed metus tristique eu. Diam suspendisse ac ipsum maecenas fermentum, aliquet imperdiet et lobortis.</div></div>
  <div class="abs" style="left:362px;top:150px;width:140px;text-align:center"><div class="t-navy" style="font-size:10px;font-weight:600">Person Name</div><div class="t-orange" style="font-size:6px">Job Title Goes Here!</div><div class="body-xs" style="margin-top:12px;color:#333">Lorem ipsum dolor sit amet, at laborum nibh duis mauris. Per ultrices lectus sed metus tristique eu. Diam suspendisse ac ipsum maecenas fermentum, aliquet imperdiet et lobortis.</div></div>
  <div class="foot-orange"></div><div class="foot-logo">SLA</div>
  <div class="foot-band"><span>© Copyright Summit Lane Advisors</span></div><div class="foot-page">6</div>
</section>

<!-- Row 4 -->
<section class="slide" style="left:51px;top:1637px">
  <div class="abs t-navy" style="left:30px;top:28px;font-size:19px;font-weight:600">Focus Areas</div>
  <div class="abs t-orange" style="left:30px;top:74px;font-size:14.5px;line-height:1.1">We work with the following<br>in digital development</div>
  <ul class="abs bullets" style="left:30px;top:140px">
    <li>Customer and user experience</li>
    <li>Systems and solutions in store</li>
    <li>Digital development and transformation</li>
    <li>Digitalization and technology</li>
  </ul>
  <div class="photo ph-cart" style="left:278px;top:0;width:232px;height:246px" role="img" aria-label="Photo of a small shopping cart on a desk with printed charts"></div>
  <div class="foot-orange"></div><div class="foot-logo">SLA</div>
  <div class="foot-band"><span>© Copyright Summit Lane Advisors</span></div><div class="foot-page">7</div>
</section>

<section class="slide" style="left:609px;top:1637px">
  <div class="photo ph-tablet" style="left:31px;top:0;width:232px;height:246px" role="img" aria-label="Photo of hands using a tablet showing charts"></div>
  <div class="abs t-navy" style="left:286px;top:28px;font-size:19px;font-weight:600">Focus Areas</div>
  <div class="abs t-orange" style="left:286px;top:70px;font-size:14.5px;line-height:1.1">We work with the following<br>technologies</div>
  <ul class="abs bullets" style="left:286px;top:118px;font-size:7.5px;line-height:1.55;width:230px">
    <li>Digital Signage</li>
    <li>Sound solutions</li>
    <li>Queue management solutions</li>
    <li>Visitor Analytics</li>
    <li>People counter technology</li>
    <li>Digital real estate solutions</li>
    <li>Media sales digital communication in store</li>
  </ul>
  <div class="foot-orange"></div><div class="foot-logo">SLA</div>
  <div class="foot-band"><span>© Copyright Summit Lane Advisors</span></div><div class="foot-page">8</div>
</section>

<!-- Row 5 -->
<section class="slide" style="left:51px;top:1959px">
  <div class="slide-title"><b>Slide Title</b> Goes Here!</div>
  <div class="abs" style="left:34px;top:74px;width:220px"><div class="item-title t-navy" style="font-size:11px">Title Goes Here!</div><div class="body-s" style="margin-top:3px">Lorem ipsum dolor sit amet, at laborum nibh duis mauris. Per ultrices lectus sed metus tristique eu. Diam suspendisse ac ipsum maecenas fermentum, aliquet imperdiet et lobortis venenatis nascetur lacus. A ac, vivamus erat nullam. Eu adipiscing pulvinar eros. Mollis malesuada vel scelerisque, ligula quam non mauris.</div></div>
  <div class="photo ph-tablet" style="left:288px;top:74px;width:252px;height:95px" role="img" aria-label="Photo of hands using a tablet with charts"></div>
  <div class="photo ph-cart" style="left:0;top:168px;width:254px;height:56px" role="img" aria-label="Photo of a shopping cart on charts"></div>
  <div class="abs" style="left:290px;top:176px;width:224px"><div class="item-title t-orange" style="font-size:11px">Title Goes Here!</div><div class="body-s" style="margin-top:3px">Lorem ipsum dolor sit amet, at laborum nibh duis mauris. Per ultrices lectus sed metus tristique eu. Diam suspendisse ac ipsum maecenas fermentum, aliquet imperdiet et lobortis venenatis nascetur lacus. A ac, vivamus erat nullam. Eu adipiscing pulvinar eros. Mollis malesuada vel scelerisque, ligula quam non mauris.</div></div>
  <div class="foot-orange"></div><div class="foot-logo">SLA</div>
  <div class="foot-band"><span>© Copyright Summit Lane Advisors</span></div><div class="foot-page">9</div>
</section>

<section class="slide" style="left:609px;top:1959px">
  <div class="slide-title"><b>Slide Title</b> Goes Here!</div>
  <div class="abs" style="left:40px;top:92px;width:150px;text-align:right"><div class="item-title" style="font-size:10px">Title Goes Here!</div><div class="body-xs" style="margin-top:6px;color:#555">Lorem ipsum dolor sit amet, at laborum nibh duis mauris. Per ultrices lectus sed metus tristique eu.</div></div>
  <div class="abs" style="left:40px;top:178px;width:150px;text-align:right"><div class="item-title" style="font-size:10px">Title Goes Here!</div><div class="body-xs" style="margin-top:6px;color:#555">Lorem ipsum dolor sit amet, at laborum nibh duis mauris. Per ultrices lectus sed metus tristique eu.</div></div>
  <div class="abs" style="left:372px;top:92px;width:130px"><div class="item-title" style="font-size:10px">Title Goes Here!</div><div class="body-xs" style="margin-top:6px;color:#555">Lorem ipsum dolor sit amet, at laborum nibh duis mauris. Per ultrices lectus sed metus tristique eu.</div></div>
  <div class="abs" style="left:372px;top:178px;width:130px"><div class="item-title" style="font-size:10px">Title Goes Here!</div><div class="body-xs" style="margin-top:6px;color:#555">Lorem ipsum dolor sit amet, at laborum nibh duis mauris. Per ultrices lectus sed metus tristique eu.</div></div>
  <div class="icon-c bg-navy" style="left:213px;top:108px;width:40px;height:40px"><svg><use href="#i-doc"/></svg></div>
  <div class="icon-c bg-orange" style="left:265px;top:88px;width:64px;height:64px;border-radius:50% 50% 50% 6px"><svg><use href="#i-search"/></svg></div>
  <div class="icon-c bg-grey" style="left:192px;top:158px;width:62px;height:62px;border-radius:50% 6px 50% 50%"><svg><use href="#i-doc"/></svg></div>
  <div class="icon-c bg-ink" style="left:265px;top:158px;width:64px;height:64px;border-radius:6px 50% 50% 50%"><svg><use href="#i-monitor"/></svg></div>
  <div class="foot-orange"></div><div class="foot-logo">SLA</div>
  <div class="foot-band"><span>© Copyright Summit Lane Advisors</span></div><div class="foot-page">10</div>
</section>

<!-- Row 6 -->
<section class="slide" style="left:51px;top:2280px">
  <div class="slide-title"><b>Slide Title</b> Goes Here!</div>
  <div class="icon-c bg-navy" style="left:38px;top:76px;width:32px;height:32px"><svg><use href="#i-bulb"/></svg></div>
  <div class="abs" style="left:80px;top:76px;width:170px"><div class="item-title t-navy" style="font-size:9px">Title Goes Here!</div><div class="body-xs" style="color:#333">Lorem ipsum dolor sit amet, at laborum nibh duis mauris. Per ultrices lectus sed metus ...</div></div>
  <div class="icon-c bg-orange" style="left:38px;top:123px;width:32px;height:32px"><svg><use href="#i-doc"/></svg></div>
  <div class="abs" style="left:80px;top:123px;width:170px"><div class="item-title t-orange" style="font-size:9px">Title Goes Here!</div><div class="body-xs" style="color:#333">Lorem ipsum dolor sit amet, at laborum nibh duis mauris. Per ultrices lectus sed metus ...</div></div>
  <div class="icon-c bg-navy" style="left:38px;top:170px;width:32px;height:32px"><svg><use href="#i-shield"/></svg></div>
  <div class="abs" style="left:80px;top:170px;width:170px"><div class="item-title t-navy" style="font-size:9px">Title Goes Here!</div><div class="body-xs" style="color:#333">Lorem ipsum dolor sit amet, at laborum nibh duis mauris. Per ultrices lectus sed metus ...</div></div>
  <div class="icon-c bg-orange" style="left:38px;top:217px;width:32px;height:32px"><svg><use href="#i-monitor"/></svg></div>
  <div class="abs" style="left:80px;top:217px;width:170px"><div class="item-title t-orange" style="font-size:9px">Title Goes Here!</div><div class="body-xs" style="color:#333">Lorem ipsum dolor sit amet, at laborum nibh duis mauris. Per ultrices lectus sed metus ...</div></div>
  <div class="icon-c bg-orange" style="left:269px;top:76px;width:32px;height:32px"><svg><use href="#i-search"/></svg></div>
  <div class="abs" style="left:311px;top:76px;width:170px"><div class="item-title t-orange" style="font-size:9px">Title Goes Here!</div><div class="body-xs" style="color:#333">Lorem ipsum dolor sit amet, at laborum nibh duis mauris. Per ultrices lectus sed metus ...</div></div>
  <div class="icon-c bg-navy" style="left:269px;top:123px;width:32px;height:32px"><svg><use href="#i-gears"/></svg></div>
  <div class="abs" style="left:311px;top:123px;width:170px"><div class="item-title t-navy" style="font-size:9px">Title Goes Here!</div><div class="body-xs" style="color:#333">Lorem ipsum dolor sit amet, at laborum nibh duis mauris. Per ultrices lectus sed metus ...</div></div>
  <div class="icon-c bg-orange" style="left:269px;top:170px;width:32px;height:32px"><svg><use href="#i-doc"/></svg></div>
  <div class="abs" style="left:311px;top:170px;width:170px"><div class="item-title t-orange" style="font-size:9px">Title Goes Here!</div><div class="body-xs" style="color:#333">Lorem ipsum dolor sit amet, at laborum nibh duis mauris. Per ultrices lectus sed metus ...</div></div>
  <div class="icon-c bg-navy" style="left:269px;top:217px;width:32px;height:32px"><svg><use href="#i-tools"/></svg></div>
  <div class="abs" style="left:311px;top:217px;width:170px"><div class="item-title t-navy" style="font-size:9px">Title Goes Here!</div><div class="body-xs" style="color:#333">Lorem ipsum dolor sit amet, at laborum nibh duis mauris. Per ultrices lectus sed metus ...</div></div>
  <div class="foot-orange"></div><div class="foot-logo">SLA</div>
  <div class="foot-band"><span>© Copyright Summit Lane Advisors</span></div><div class="foot-page">11</div>
</section>

<section class="slide" style="left:609px;top:2280px">
  <div class="slide-title"><b>Slide Title</b> Goes Here!</div>
  <div class="abs bg-navy" style="left:0;top:96px;width:540px;height:134px"></div>
  <svg class="abs" style="left:0;top:0" width="540" height="303" aria-hidden="true">
    <g stroke="#fff" stroke-width="1" fill="none">
      <line x1="110" y1="134" x2="155" y2="134"/><line x1="110" y1="190" x2="155" y2="190"/>
      <line x1="195" y1="134" x2="228" y2="134"/><line x1="195" y1="190" x2="228" y2="190"/>
      <line x1="312" y1="134" x2="344" y2="134"/><line x1="312" y1="190" x2="344" y2="190"/>
      <line x1="384" y1="134" x2="430" y2="134"/><line x1="384" y1="190" x2="430" y2="190"/>
    </g>
  </svg>
  <div class="icon-c" style="left:155px;top:114px;width:40px;height:40px;border:2px solid #fff"><svg><use href="#i-search"/></svg></div>
  <div class="icon-c" style="left:155px;top:170px;width:40px;height:40px;border:2px solid #fff"><svg><use href="#i-doc"/></svg></div>
  <div class="icon-c" style="left:344px;top:114px;width:40px;height:40px;border:2px solid #fff"><svg><use href="#i-tools"/></svg></div>
  <div class="icon-c" style="left:344px;top:170px;width:40px;height:40px;border:2px solid #fff"><svg><use href="#i-chart"/></svg></div>
  <div class="abs" style="left:224px;top:78px;width:94px;height:174px;background:var(--ink);border-radius:12px"></div>
  <div class="abs bg-orange" style="left:229px;top:90px;width:84px;height:144px;border-radius:3px"></div>
  <div class="abs h-white" style="left:229px;top:146px;width:84px;text-align:center;font-size:22px;font-weight:700">SLA</div>
  <div class="abs" style="left:265px;top:238px;width:12px;height:12px;border-radius:50%;background:#fff"></div>
  <div class="abs h-white" style="left:30px;top:112px;width:80px;text-align:center"><div style="font-size:9px">Title Goes Here!</div><div style="font-size:5px;line-height:1.25;margin-top:2px">Lorem ipsum dolor sit amet, at laborum nibh duis mauris. Per ultrices lectus sed metus tristique eu.</div></div>
  <div class="abs h-white" style="left:30px;top:168px;width:80px;text-align:center"><div style="font-size:9px">Title Goes Here!</div><div style="font-size:5px;line-height:1.25;margin-top:2px">Lorem ipsum dolor sit amet, at laborum nibh duis mauris. Per ultrices lectus sed metus tristique eu.</div></div>
  <div class="abs h-white" style="left:400px;top:112px;width:100px"><div style="font-size:9px">Title Goes Here!</div><div style="font-size:5px;line-height:1.25;margin-top:2px">Lorem ipsum dolor sit amet, at laborum nibh duis mauris. Per ultrices lectus sed metus tristique eu.</div></div>
  <div class="abs h-white" style="left:400px;top:168px;width:100px"><div style="font-size:9px">Title Goes Here!</div><div style="font-size:5px;line-height:1.25;margin-top:2px">Lorem ipsum dolor sit amet, at laborum nibh duis mauris. Per ultrices lectus sed metus tristique eu.</div></div>
  <div class="foot-orange"></div><div class="foot-logo">SLA</div>
  <div class="foot-band"><span>© Copyright Summit Lane Advisors</span></div><div class="foot-page">12</div>
</section>

<!-- Row 7 -->
<section class="slide" style="left:51px;top:2602px">
  <div class="slide-title"><b>Slide Title</b> Goes Here!</div>
  <svg class="abs" style="left:0;top:0" width="300" height="260" role="img" aria-label="Bar chart with three series across four categories">
    <g font-family="Montserrat, sans-serif" font-size="5.5" fill="#555">
      <g stroke="#e2e4e7" stroke-width="0.6">
        <line x1="52" y1="89" x2="290" y2="89"/><line x1="52" y1="111.5" x2="290" y2="111.5"/><line x1="52" y1="134" x2="290" y2="134"/>
        <line x1="52" y1="156.5" x2="290" y2="156.5"/><line x1="52" y1="179" x2="290" y2="179"/><line x1="52" y1="201.5" x2="290" y2="201.5"/>
        <line x1="52" y1="224" x2="290" y2="224"/>
      </g>
      <text x="44" y="91">6</text><text x="44" y="113">5</text><text x="44" y="136">4</text><text x="44" y="158">3</text><text x="44" y="181">2</text><text x="44" y="203">1</text><text x="44" y="226">0</text>
      <rect x="66" y="127" width="8" height="97" fill="#0b4a92"/><rect x="78" y="170" width="8" height="54" fill="#f28a1c"/><rect x="90" y="179" width="8" height="45" fill="#222426"/>
      <rect x="126" y="168" width="8" height="56" fill="#0b4a92"/><rect x="138" y="125" width="8" height="99" fill="#f28a1c"/><rect x="150" y="179" width="8" height="45" fill="#222426"/>
      <rect x="186" y="145" width="8" height="79" fill="#0b4a92"/><rect x="198" y="184" width="8" height="40" fill="#f28a1c"/><rect x="210" y="156" width="8" height="68" fill="#222426"/>
      <rect x="246" y="123" width="8" height="101" fill="#0b4a92"/><rect x="258" y="161" width="8" height="63" fill="#f28a1c"/><rect x="270" y="111" width="8" height="113" fill="#222426"/>
      <text x="68" y="234">Category 1</text><text x="128" y="234">Category 2</text><text x="188" y="234">Category 3</text><text x="248" y="234">Category 4</text>
    </g>
  </svg>
  <div class="abs" style="left:330px;top:85px;width:6px;height:6px;border-radius:50%;background:var(--navy)"></div>
  <div class="abs" style="left:346px;top:82px;width:160px"><div class="t-navy" style="font-size:8.5px">Title Goes Here!</div><div class="body-xs" style="color:#444">Lorem ipsum dolor sit amet, at laborum nibh duis mauris. Per ultrices lectus sed metus tristique eu. Diam suspendisse ac ipsum</div></div>
  <div class="abs" style="left:330px;top:139px;width:6px;height:6px;border-radius:50%;background:var(--orange)"></div>
  <div class="abs" style="left:346px;top:136px;width:160px"><div class="t-orange" style="font-size:8.5px">Title Goes Here!</div><div class="body-xs" style="color:#444">Lorem ipsum dolor sit amet, at laborum nibh duis mauris. Per ultrices lectus sed metus tristique eu. Diam suspendisse ac ipsum</div></div>
  <div class="abs" style="left:330px;top:193px;width:6px;height:6px;border-radius:50%;background:var(--ink)"></div>
  <div class="abs" style="left:346px;top:190px;width:160px"><div style="font-size:8.5px">Title Goes Here!</div><div class="body-xs" style="color:#444">Lorem ipsum dolor sit amet, at laborum nibh duis mauris. Per ultrices lectus sed metus tristique eu. Diam suspendisse ac ipsum</div></div>
  <div class="foot-orange"></div><div class="foot-logo">SLA</div>
  <div class="foot-band"><span>© Copyright Summit Lane Advisors</span></div><div class="foot-page">13</div>
</section>

<section class="slide" style="left:609px;top:2602px">
  <div class="slide-title"><b>Slide Title</b> Goes Here!</div>
  <div class="abs" style="left:0;top:90px;width:185px;height:68px;background:var(--light)"></div>
  <div class="abs" style="left:0;top:163px;width:185px;height:68px;background:var(--light)"></div>
  <div class="abs" style="left:355px;top:90px;width:185px;height:68px;background:var(--light)"></div>
  <div class="abs" style="left:355px;top:163px;width:185px;height:68px;background:var(--light)"></div>
  <div class="abs bg-navy h-white" style="left:0;top:90px;width:20px;height:68px;display:flex;align-items:center;justify-content:center"><span style="transform:rotate(-90deg);font-size:11px;font-weight:600">20%</span></div>
  <div class="abs h-white" style="left:0;top:163px;width:20px;height:68px;background:#c8cacd;display:flex;align-items:center;justify-content:center"><span style="transform:rotate(-90deg);font-size:11px;font-weight:600">40%</span></div>
  <div class="abs bg-orange h-white" style="left:520px;top:90px;width:20px;height:68px;display:flex;align-items:center;justify-content:center"><span style="transform:rotate(90deg);font-size:11px;font-weight:600">80%</span></div>
  <div class="abs bg-ink h-white" style="left:520px;top:163px;width:20px;height:68px;display:flex;align-items:center;justify-content:center"><span style="transform:rotate(90deg);font-size:11px;font-weight:600">60%</span></div>
  <div class="abs" style="left:28px;top:100px;width:120px;text-align:center"><div style="font-size:9px">Title Goes Here!</div><div class="body-xs" style="color:#444">Lorem ipsum dolor sit amet, at laborum nibh duis mauris. Per ultrices lectus sed metus tristique eu. Diam suspendisse.</div></div>
  <div class="abs" style="left:28px;top:173px;width:120px;text-align:center"><div style="font-size:9px">Title Goes Here!</div><div class="body-xs" style="color:#444">Lorem ipsum dolor sit amet, at laborum nibh duis mauris. Per ultrices lectus sed metus tristique eu. Diam suspendisse.</div></div>
  <div class="abs" style="left:392px;top:100px;width:120px;text-align:center"><div style="font-size:9px">Title Goes Here!</div><div class="body-xs" style="color:#444">Lorem ipsum dolor sit amet, at laborum nibh duis mauris. Per ultrices lectus sed metus tristique eu. Diam suspendisse.</div></div>
  <div class="abs" style="left:392px;top:173px;width:120px;text-align:center"><div style="font-size:9px">Title Goes Here!</div><div class="body-xs" style="color:#444">Lorem ipsum dolor sit amet, at laborum nibh duis mauris. Per ultrices lectus sed metus tristique eu. Diam suspendisse.</div></div>
  <svg class="abs" style="left:0;top:0" width="540" height="303" role="img" aria-label="Pie chart with four segments">
    <circle cx="270" cy="162" r="92" fill="#fff"/>
    <g stroke="#fff" stroke-width="3" font-family="Montserrat, sans-serif" font-weight="600" font-size="11">
      <path d="M270 162 L270 82 A80 80 0 0 1 310 231.3 Z" fill="#f28a1c"/>
      <path d="M270 162 L310 231.3 A80 80 0 0 1 194.8 189.4 Z" fill="#222426"/>
      <path d="M270 162 L194.8 189.4 A80 80 0 0 1 208.7 110.6 Z" fill="#c8cacd"/>
      <path d="M270 162 L208.7 110.6 A80 80 0 0 1 270 82 Z" fill="#0b4a92"/>
    </g>
    <g font-family="Montserrat, sans-serif" font-weight="600" font-size="10" fill="#fff">
      <text x="237" y="102">20%</text><text x="299" y="164">80%</text><text x="253" y="221">60%</text><text x="203" y="158">40%</text>
    </g>
  </svg>
  <div class="foot-orange"></div><div class="foot-logo">SLA</div>
  <div class="foot-band"><span>© Copyright Summit Lane Advisors</span></div><div class="foot-page">14</div>
</section>

<!-- Row 8 -->
<section class="slide" style="left:51px;top:2923px">
  <div class="slide-title"><b>Slide Title</b> Goes Here!</div>
  <table class="data">
    <tr><th style="width:180px">Heading Goes Here!</th><th>Heading 1</th><th>Heading 2</th><th>Heading 3</th><th class="hl">Heading 4</th></tr>
    <tr><td>Lorem ipsum dolor sit amet ...</td><td>23</td><td>34</td><td>09</td><td>98</td></tr>
    <tr><td>Lorem ipsum dolor sit amet ...</td><td>44</td><td>89</td><td>12</td><td>78</td></tr>
    <tr><td>Lorem ipsum dolor sit amet ...</td><td>56</td><td>99</td><td>89</td><td>98</td></tr>
    <tr><td>Lorem ipsum dolor sit amet ...</td><td>78</td><td>88</td><td>56</td><td>88</td></tr>
  </table>
  <div class="foot-orange"></div><div class="foot-logo">SLA</div>
  <div class="foot-band"><span>© Copyright Summit Lane Advisors</span></div><div class="foot-page">15</div>
</section>

<section class="slide" style="left:609px;top:2923px;background:#111">
  <div class="photo ph-map" style="left:0;top:0;width:540px;height:303px" role="img" aria-label="Street map of the office location, darkened on the left"></div>
  <div class="abs t-navy" style="left:44px;top:100px;font-size:26px;font-weight:700;color:#3f7fd0">SLA</div>
  <div class="abs t-orange" style="left:44px;top:134px;font-size:12px;font-weight:600">Contact Us</div>
  <div class="abs h-white" style="left:44px;top:152px;font-size:6.5px">Granvägen 8, 236 40 Sjöholm</div>
  <div class="abs contact" style="left:44px;top:188px">
    <div><svg><use href="#i-phone"/></svg>+46-700000123</div>
    <div><svg><use href="#i-at"/></svg>info@summitlaneadvisors.se</div>
    <div><svg><use href="#i-globe"/></svg>https://summitlaneadvisors.se</div>
  </div>
</section>

<!-- Closing -->
<section class="slide" style="left:330px;top:3245px;background:#0c0c0d">
  <div class="photo" style="left:0;top:0;width:540px;height:303px;background:radial-gradient(ellipse at 68% 55%,#3a3632 0%,#1c1a19 40%,#0a0a0b 75%)" role="img" aria-label="Dark photo of a hand holding a smartphone with glowing app icons"></div>
  <div class="abs t-orange" style="left:50px;top:46px;font-size:19px;font-weight:600">Thank You!</div>
  <div class="abs h-white" style="left:50px;top:72px;font-size:11px">for your attention and valuable time</div>
  <div class="abs" style="left:44px;top:140px;font-size:26px;font-weight:700;color:#3f7fd0">SLA</div>
  <div class="abs t-orange" style="left:44px;top:184px;font-size:12px;font-weight:600">Contact Us</div>
  <div class="abs contact" style="left:44px;top:212px">
    <div><svg><use href="#i-phone"/></svg>+46-700000123</div>
    <div><svg><use href="#i-at"/></svg>info@summitlaneadvisors.se</div>
    <div><svg><use href="#i-globe"/></svg>https://summitlaneadvisors.se</div>
  </div>
</section>

</body>
</html>
```